New online business - used mobile phones - needs unique eye catching web design that sets it apart

The Handset Bazaar
We are a new business looking for a rapid response for our web site design. We don't want a normal website....... we need to be creative - most important PLEASE view the attached files uploaded 3 March to ensure you get us :)
.
The Handset Bazaar buys new and damaged mobile phones from the public. A simple process they complete to sell their mobile to us; we want our website to reflect this.
Our website needs to be modern, edgy and fun, not corporate and definitely not like any other mobile phone buying site in the world today!!
Our name was taken from a play on the share/stock market which we have tried to bring into the design ....... it hasn't worked with early designs submitted. Now taking a different approach. Refer to new attached files which should help you visualise our concept.

We like layout from Sketch Flock – rtlbenoviqs #7132809 design as this is very close to our layout vision.
The first page to tell the public what we do, how we do it, and then they click to accept the instant online quote. (page two they complete details about the mobiles model & condition they are selling, then page three complete their personal details).
Our background preference is dark, blackboard or dark with slight texture
a) We love white on black/dark background either typewriter font or look like hand drawn refer to attached files & heronandfig.com.au site to see. Would Label font work???

b) Where the light blue colour is on #7132809 this needs to be like chromavell colour classic green, fern green or bright green, not fluorescent lime green or an insipid green.

c) The banner says The Handset Bazaar is open........... for buying mobiles for cash $$$ (we need people to know we BUY used/damaged phones)

d) We love colour either solid colour or looks like it has been coloured in on our dark background. Open to white or pastel background versions refer to attached coffee file.
We like Chromavell Orange 021,Haute Red,Dazzling Blue, Cyan Blue, Beetroot Purple, Island Green.
e) How it works – underneath this title put Our deal …………. It’s easy as…………..quote, post, get paid!!!
Quote – first circle hand drawn icon showing mobile phone & $ sign. Underneath it says .....Obtain Quote for Model & Condition
Post – second circle hand drawn icon show parcel. Underneath it says Free Post
Paid – third circle hand drawn icon showing large $ sign. Underneath it says Payment in Two Days
Plans - is swapped for wording- Get Market Quote with a large button which says GO or CLICK HERE (they click on the button & it takes them to the next page)
f) FAQ
Allow for six FAQ’s we will forward correct content to you for final design layout.

g) About Us
Please allow about a paragraph of text here, we will forward correct content to you for final design layout.
h) Contact Us
At the bottom where normal website have ………. home, contact details, blog, etc, please only put Email us & Call us, then social media icons for QV, Work Nest and Chirpel

I) LOGO We don’t have one yet, just put The Handset Bazaar at the top & it needs to be large sized font ................we are new and we need to push our name
If you are not clear on our vision ..........please email me and I will reply very quickly.
Thank you for taking the time to read & understand & get us:)

Target Market(s)

20-45 years any body with a spare smart phone that is lying around and they can get cash for. Target market could be slightly older to 50 but focus of 20-40's

Industry/Entity Type

Business

Number of Pages Required

3 page

Font styles to use
Other font styles liked:
• handwritten font or typewriter font

Requirements
Must have
• Read only attached files dated 4 March, tech error with other files, being removed.
• 1 Layout design of Sketch Flock – rtlbenoviqs #7132809
• 2 Hand drawn icons - refer to files
• 3 White font needs to look like hand written refer to heronandfig.com.au or typewriter font - large size font
• 4 Main colours are Black or dark background, green with white text, preference is hand drawn font. The three circles for quote, post & pay with hand drawn icons can be any colour ...... Purple for quote, orange for post & green for paid
• 5 Big green button underneath 3 circles quote/post/pay - customers click on big button to get instant quote
Nice to have
• Coloured in hand drawings as per file
• Great Hand drawings coloured in
Should not have
• NO template designs so it look like you just put some text & a photo. Don't fill the page with mobile phones, one or two is ok, mobile phone pictures date so fast.
• Cartoons

```html
<!DOCTYPE html>
<html lang="en">
<head>
<meta charset="utf-8">
<title>The Handset Bazaar</title>
<link rel="stylesheet" href="https://fonts.googleapis.com/css2?family=Gochi+Hand&family=Kalam:wght@400;700&display=swap">
<style>
  :root {
    --board: #373737;
    --chalk: #f4f4f2;
    --chalk-soft: #d8d8d4;
    --gold: #c99a27;
    --phone-green: #1cb35a;
    --phone-yellow: #f5d90a;
    --phone-blue: #3a92de;
    --phone-red: #f0443a;
    --icon-fill: #c9c3bb;
    --icon-line: #e08a1e;
  }
  * { box-sizing: border-box; margin: 0; padding: 0; }
  html, body { width: 711px; height: 1200px; overflow: hidden; background: var(--board); }
  .page {
    position: relative; width: 711px; height: 1200px; background: var(--board);
    color: var(--chalk); font-family: "Gochi Hand", cursive;
  }
  .abs { position: absolute; }
  a { color: inherit; text-decoration: none; }

  .brand-badge {
    left: 77px; top: 7px; width: 140px; height: 140px; border-radius: 50%;
    background: var(--gold); display: flex; align-items: center; justify-content: center;
    text-align: center; font-size: 22px; line-height: 24px; color: var(--chalk); padding: 0 14px;
  }
  .hero-headline {
    left: 64px; top: 168px; width: 300px; font-size: 30px; line-height: 42px;
    color: var(--gold); font-weight: 400; white-space: nowrap;
  }
  .hero-phones {
    left: 368px; top: 63px; width: 271px; height: 198px; border-radius: 10px;
    background: linear-gradient(90deg, var(--phone-green) 0%, var(--phone-yellow) 25%, var(--phone-yellow) 48%, var(--phone-blue) 50%, var(--phone-blue) 68%, var(--phone-red) 70%);
  }
  .chalk-rule { height: 2px; background: var(--chalk-soft); border-radius: 2px; }

  .section-title { text-align: center; color: var(--gold); font-weight: 400; }
  .how-title { left: 0; width: 711px; top: 382px; font-size: 42px; }
  .how-underline { left: 263px; top: 436px; width: 196px; height: 3px; background: var(--chalk); }

  .step { width: 170px; text-align: center; }
  .step-circle {
    width: 144px; height: 144px; margin: 0 auto; border-radius: 50%;
    border: 5px solid var(--chalk); display: flex; align-items: center; justify-content: center;
  }
  .step-icon { width: 62px; height: 62px; border-radius: 50%; background: var(--icon-fill); border: 4px solid var(--icon-line); }
  .step-label { font-size: 31px; margin-top: 14px; }

  .quote-button {
    left: 215px; top: 752px; width: 281px; height: 67px; border: 3px solid var(--chalk);
    display: flex; align-items: center; padding-left: 28px; font-size: 20px; letter-spacing: 0.5px;
  }
  .go-mark {
    position: absolute; left: 207px; top: 6px; width: 50px; height: 50px; border-radius: 50%;
    border: 3px solid var(--gold); color: var(--gold); font-size: 18px;
    display: flex; align-items: center; justify-content: center;
  }

  .about-title { left: 87px; width: 151px; top: 876px; font-size: 28px; }
  .faq-title { left: 285px; width: 330px; top: 876px; font-size: 28px; }
  .about-underline { left: 87px; top: 918px; width: 151px; height: 3px; background: var(--chalk); }
  .faq-underline { left: 285px; top: 918px; width: 330px; height: 3px; background: var(--chalk); }

  .about-copy {
    left: 77px; top: 942px; width: 170px; font-family: "Kalam", cursive; font-weight: 700;
    font-size: 8.6px; line-height: 13.1px; text-align: center;
  }
  .faq-col { width: 162px; font-family: "Kalam", cursive; text-align: center; }
  .faq-item { height: 76px; }
  .faq-q { font-weight: 700; font-size: 9px; line-height: 13px; }
  .faq-a { font-size: 7.4px; line-height: 13px; color: var(--chalk-soft); margin-top: 4px; }

  .footer-row {
    left: 74px; top: 1118px; width: 564px; height: 34px; display: flex; align-items: center;
    font-family: "Kalam", cursive; font-size: 11px; font-weight: 700; white-space: nowrap;
  }
  .contact { display: flex; align-items: center; gap: 10px; }
  .contact-email { width: 222px; padding-left: 10px; }
  .contact-phone { width: 160px; }
  .social-list { display: flex; gap: 10px; margin-left: auto; }
  .social-link {
    display: flex; align-items: center; gap: 4px; font-family: "Gochi Hand", cursive;
    font-size: 12px; font-weight: 400; white-space: nowrap;
  }
  .social-dot { width: 12px; height: 12px; border: 1.5px solid var(--chalk); border-radius: 50%; flex: none; }
</style>
</head>
<body>
<main class="page">

  <header>
    <div class="abs brand-badge">The Handset Bazaar</div>
    <h1 class="abs hero-headline">The Handset Bazaar is<br>open for buying<br>mobiles for cash $$$</h1>
    <div class="abs hero-phones" role="img" aria-label="Four smartphones in green, yellow, blue and red, overlapping in a row"></div>
  </header>

  <div class="abs chalk-rule" style="left:74px; top:329px; width:564px;"></div>

  <section aria-labelledby="how">
    <h2 id="how" class="abs section-title how-title">How It Works</h2>
    <div class="abs how-underline"></div>

    <div class="abs step" style="left:74px; top:495px;">
      <div class="step-circle"><div class="step-icon" role="img" aria-label="Hand drawn mobile phone icon"></div></div>
      <p class="step-label">Quote</p>
    </div>
    <div class="abs step" style="left:271px; top:495px;">
      <div class="step-circle"><div class="step-icon" role="img" aria-label="Hand drawn parcel icon"></div></div>
      <p class="step-label">Post</p>
    </div>
    <div class="abs step" style="left:470px; top:495px;">
      <div class="step-circle"><div class="step-icon" role="img" aria-label="Hand drawn money bag icon"></div></div>
      <p class="step-label" style="margin-top:20px">Paid</p>
    </div>

    <a class="abs quote-button">Get Free Quote <span class="go-mark">Go</span></a>
  </section>

  <div class="abs chalk-rule" style="left:74px; top:851px; width:564px;"></div>

  <section aria-labelledby="about">
    <h2 id="about" class="abs section-title about-title">About Us</h2>
    <div class="abs about-underline"></div>
    <p class="abs about-copy">Lorem Ipsum is simply dummy text of the printing and typesetting industry. Lorem Ipsum has been the industry's standard dummy text ever since the 1500s, when an unknown printer took a galley of type and scrambled it to make a type specimen book. It has survived not only five centuries, but also the leap into electronic typesetting, remaining essentially unchanged. It was popularised in the 1960s with the re-</p>
  </section>

  <section aria-labelledby="faq">
    <h2 id="faq" class="abs section-title faq-title">FAQ</h2>
    <div class="abs faq-underline"></div>
    <div class="abs faq-col" style="left:273px; top:945px;">
      <div class="faq-item">
        <p class="faq-q">3&nbsp; Lorem Ipsum is simply dummy text of the printing and typesetting</p>
        <p class="faq-a">There are many variations of passages of Lorem Ipsum available, but the majority have suffered alteration in some form, by</p>
      </div>
      <div class="faq-item">
        <p class="faq-q">4&nbsp; Lorem Ipsum is simply dummy text of the printing and typesetting</p>
        <p class="faq-a">There are many variations of passages of Lorem Ipsum available, but the majority have</p>
      </div>
    </div>
    <div class="abs faq-col" style="left:468px; top:945px;">
      <div class="faq-item">
        <p class="faq-q">5&nbsp; Lorem Ipsum is simply dummy text of the printing and typesetting</p>
        <p class="faq-a">There are many variations of passages of Lorem Ipsum available, but the majority have suffered alteration in some form, by</p>
      </div>
      <div class="faq-item">
        <p class="faq-q">6&nbsp; Lorem Ipsum is simply dummy text of the printing and typesetting</p>
        <p class="faq-a">There are many variations of passages of Lorem Ipsum available, but the majority have</p>
      </div>
    </div>
  </section>

  <div class="abs chalk-rule" style="left:74px; top:1107px; width:564px;"></div>

  <footer class="abs footer-row">
    <div class="contact contact-email">
      <svg width="28" height="18" viewBox="0 0 28 18" aria-hidden="true">
        <rect x="1" y="1" width="26" height="16" fill="none" stroke="#f4f4f2" stroke-width="1.6"/>
        <path d="M1 1 L14 10 L27 1" fill="none" stroke="#f4f4f2" stroke-width="1.6"/>
      </svg>
      <span>hello@handsetbazaar.com</span>
    </div>
    <div class="contact contact-phone">
      <svg width="26" height="22" viewBox="0 0 26 22" aria-hidden="true">
        <path d="M2 8 Q13 0 24 8 L21 11 L18 8 L8 8 L5 11 Z" fill="#f4f4f2"/>
        <rect x="5" y="11" width="16" height="10" rx="2" fill="none" stroke="#f4f4f2" stroke-width="1.6"/>
        <circle cx="13" cy="16" r="2.5" fill="#f4f4f2"/>
      </svg>
      <span>321-654-0987</span>
    </div>
    <nav class="social-list" aria-label="Social media">
      <a class="social-link"><span class="social-dot"></span>QV</a>
      <a class="social-link"><span class="social-dot"></span>Work Nest</a>
      <a class="social-link"><span class="social-dot"></span>Chirpel</a>
    </nav>
  </footer>

</main>
</body>
</html>
```